Manufacturing company needs new business card.

I need a unique Business Card that will truly stand out. Nothing too busy. Simple is good, right? Not looking for a standard design either. No cookie cutter layout. I am just looking for something interesting and a bit different. Does't have to completely off the wall crazy, just not your run of the mill business card. Clean and modern with a touch of industrial.

Target Market(s)

Air conditioning industry, Architects, builders.

Industry/Entity Type

Business

Contact Information for Business Card

Details to be included on card are:

Peter Vance
Managing Director

T: 1300 847 519
M: 0428 593 174
W: www.brenvaleworks.com.au
E: peter.vance@brenvaleworks.com.au
A: 58 Harwick Lane, Sydney NSW 2000

Font styles to use
Sans Serif

Colors
0355a3
848484
fbfbfb

Requirements
Must have
• Card design must be landscape.

```html
<!DOCTYPE html>
<html lang="en">
<head>
<meta charset="utf-8">
<title>Brenvale Works – Business Card</title>
<link href="https://fonts.googleapis.com/css2?family=Didact+Gothic&family=Mulish:wght@600&display=swap" rel="stylesheet">
<style>
  :root{
    --stage:#5e5e5e;
    --card:#04040a;
    --blue:#1f55b0;
    --grey:#848484;
    --text:#9a9aa0;
    --rule:#3a3a40;
  }
  html,body{margin:0;padding:0;overflow:hidden}
  body{width:1200px;height:1200px;background:var(--stage);position:relative;font-family:"Didact Gothic",sans-serif}
  .card{position:absolute;left:280px;width:640px;height:363px;background:var(--card);box-shadow:0 4px 10px rgba(0,0,0,.45)}
  .card--front{top:209px}
  .card--back{top:629px}

  .brand{position:absolute;left:133px;top:158px;display:flex;align-items:center;gap:18px}
  .brand__square{width:50px;height:50px;background:var(--grey)}
  .brand__name{font-family:"Mulish",sans-serif;font-weight:600;font-size:30px;color:var(--grey);letter-spacing:.2px}

  .mark{position:absolute;left:69px;top:121px;width:121px;height:121px;background:var(--blue);border-radius:4px}
  .divider{position:absolute;left:245px;top:75px;width:1px;height:224px;background:var(--rule)}

  .details{position:absolute;left:269px;top:104px;color:var(--text)}
  .details__name{font-family:"Mulish",sans-serif;font-weight:600;font-size:22px;color:var(--blue);margin:0;line-height:1}
  .details__title{font-size:16px;margin:6px 0 0;line-height:1}
  .contacts{list-style:none;margin:16px 0 0;padding:0}
  .contacts li{display:flex;align-items:center;height:21.5px;font-size:16px}
  .contacts svg{width:14px;height:14px;margin-right:15px;margin-left:2px;fill:var(--blue);flex:none}
  .details__address{font-size:16px;margin:15px 0 0}
</style>
</head>
<body>
  <section class="card card--front">
    <div class="brand">
      <span class="brand__square"></span>
      <span class="brand__name">Brenvale Works</span>
    </div>
  </section>

  <section class="card card--back">
    <div class="mark"></div>
    <div class="divider"></div>
    <div class="details">
      <h1 class="details__name">Peter Vance</h1>
      <p class="details__title">Managing Director</p>
      <ul class="contacts">
        <li><svg viewBox="0 0 16 16"><path d="M1 6c0-3 3-4 7-4s7 1 7 4l-3 1-1-2H5L4 7 1 6zm3 2h8l2 6H2l2-6zm4 1.5a2 2 0 100 4 2 2 0 000-4z"/></svg>1300 847 519</li>
        <li><svg viewBox="0 0 16 16"><path d="M4 0h8a1 1 0 011 1v14a1 1 0 01-1 1H4a1 1 0 01-1-1V1a1 1 0 011-1zm1 2v10h6V2H5zm3 11a1 1 0 100 2 1 1 0 000-2z"/></svg>0428 593 174</li>
        <li><svg viewBox="0 0 16 16"><path d="M0 3h16v10H0V3zm2 1.5V12h12V4.5L8 9 2 4.5z"/></svg>peter.vance@brenvaleworks.com.au</li>
        <li><svg viewBox="0 0 16 16"><path d="M8 0a8 8 0 110 16A8 8 0 018 0zm0 1.5c-.9 1-1.5 2.8-1.6 4.8h3.2C9.5 4.3 8.9 2.5 8 1.5zM1.6 7.3h3.7c0-1.8.4-3.5 1-4.8a6.5 6.5 0 00-4.7 4.8zm0 1.4a6.5 6.5 0 004.7 4.8c-.6-1.3-1-3-1-4.8H1.6zm4.8 0c.1 2 .7 3.8 1.6 4.8.9-1 1.5-2.8 1.6-4.8H6.4zm4.3 0c0 1.8-.4 3.5-1 4.8a6.5 6.5 0 004.7-4.8h-3.7zm3.7-1.4a6.5 6.5 0 00-4.7-4.8c.6 1.3 1 3 1 4.8h3.7z"/></svg>www.brenvaleworks.com.au</li>
      </ul>
      <p class="details__address">58 Harwick Lane, Sydney NSW 2000</p>
    </div>
  </section>
</body>
</html>
```